[AMAZING DESIGN NEEDED] Women's Fishing Squeeze Page

I need a professional design for a landing page that is going to collect email addresses.

You can use the creatives already on the page or you can pull images from the facebook/instagram pages.
https://www.facebook.com/LakesLuresBoots
https://www.instagram.com/lakesluresandboots/

This is the page that needs designed: https://lakesluresandboots.example/email-opt-in/

See attached for examples.

Target Market(s)

Women who like to go fishing

Industry/Entity Type

Fishing

Number of Pages Required

1 page

Font styles to use
Sans Serif

Requirements
Must have
• excellent design. Call to actions.

```html
<!DOCTYPE html>
<html lang="en">
<head>
<meta charset="utf-8">
<title>Lakes, Lures &amp; Boots — Sign Up Today</title>
<link href="https://fonts.googleapis.com/css2?family=Jost:wght@400;500;600&family=Dancing+Script:wght@600&display=swap" rel="stylesheet">
<style>
  :root {
    --teal: #0b7b7b;
    --brown: #4a3a2d;
    --sand: #c9b5a3;
    --link: #86613f;
    --field: #e4e4e4;
    --white: #ffffff;
  }
  * { box-sizing: border-box; margin: 0; padding: 0; }
  html, body { width: 1200px; height: 1178px; overflow: hidden; }
  body { position: relative; font-family: 'Jost', sans-serif; color: var(--brown); background: var(--sand); }
  a { color: inherit; text-decoration: none; }

  .hero-photo {
    position: absolute; left: 0; top: 0; width: 1200px; height: 768px;
    background:
      linear-gradient(90deg, rgba(70,60,50,.55) 0%, rgba(120,110,95,.35) 40%, rgba(150,160,160,0) 60%),
      linear-gradient(180deg, #b8c4c8 0%, #8fa08a 22%, #7e8d88 45%, #93a2a6 70%, #7f8d8e 100%);
  }
  .site-header {
    position: absolute; left: 0; top: 0; width: 1200px; height: 120px;
    background: rgba(240,242,244,.82);
  }
  .brand {
    position: absolute; left: 88px; top: 40px;
    font-size: 20px; font-weight: 600; color: var(--teal); letter-spacing: .5px;
  }
  .brand-dot {
    display: inline-block; width: 12px; height: 12px; border-radius: 50%;
    background: var(--teal); margin-right: 8px; vertical-align: 1px;
  }
  .utility { position: absolute; top: 33px; font-size: 15.5px; font-weight: 500; color: var(--brown); }
  .utility .sep { margin: 0 14px; }
  .icon-btn {
    position: absolute; top: 29px; width: 32px; height: 32px; border-radius: 50%;
    background: var(--brown); display: flex; align-items: center; justify-content: center;
  }
  .cart {
    position: absolute; left: 895px; top: 29px; width: 128px; height: 32px; border-radius: 16px;
    background: var(--teal); color: var(--white); font-size: 15.5px; font-weight: 500;
    display: flex; align-items: center; justify-content: center; gap: 8px;
  }
  .main-nav {
    position: absolute; top: 84px; left: 422px; width: 688px;
    display: flex; justify-content: space-between;
    font-size: 15.5px; font-weight: 500; letter-spacing: .4px; color: var(--brown);
  }

  .signup-accent {
    position: absolute; left: 656px; top: 204px; width: 456px; height: 408px;
    background: var(--teal); border-radius: 10px;
  }
  .signup-card {
    position: absolute; left: 616px; top: 236px; width: 464px; height: 416px;
    background: var(--white); border-radius: 12px; padding: 0 32px;
    text-align: center;
  }
  .signup-title {
    font-family: 'Dancing Script', cursive; font-weight: 600; font-size: 62px;
    color: var(--brown); margin-top: 30px; line-height: 80px;
  }
  .signup-sub { font-size: 23.5px; color: var(--brown); margin-top: 2px; letter-spacing: .4px; }
  .signup-sub em { color: var(--teal); }
  .field {
    display: block; width: 400px; height: 40px; border-radius: 20px;
    background: var(--field); border: 0; margin-top: 16px;
    padding: 0 20px; font: 400 15.5px 'Jost', sans-serif; color: var(--brown); text-align: left;
    line-height: 40px;
  }
  .field:first-of-type { margin-top: 19px; }
  .cta {
    display: block; width: 400px; height: 40px; border-radius: 20px; margin-top: 16px;
    background: var(--teal); color: var(--white); border: 0;
    font: 500 15px 'Jost', sans-serif; letter-spacing: .6px;
  }

  .site-footer { position: absolute; left: 0; top: 768px; width: 1200px; height: 410px; }
  .col { position: absolute; top: 75px; }
  .col h3 { font-size: 19.5px; font-weight: 500; color: var(--brown); letter-spacing: .4px; margin-bottom: 10px; }
  .col li { list-style: none; font-size: 15px; line-height: 24px; color: var(--link); letter-spacing: .3px; }
  .phone { font-size: 16.5px; font-weight: 500; color: var(--link); letter-spacing: .4px; }
  .connect { margin-top: 22px; }
  .social { display: flex; gap: 8px; margin-top: 14px; }
  .social span { width: 32px; height: 32px; border-radius: 50%; background: var(--brown); }
  .social span.active { background: var(--teal); }
  .news-copy { font-size: 15px; line-height: 17px; color: var(--link); letter-spacing: .3px; width: 320px; }
  .news-input {
    display: block; margin-top: 20px; width: 320px; height: 40px; border-radius: 20px;
    border: 1px solid var(--brown); background: var(--white); padding: 0 16px;
    font: 400 15px 'Jost', sans-serif; color: var(--brown); line-height: 38px;
  }
  .news-btn {
    display: block; margin-top: 8px; width: 128px; height: 40px; border-radius: 20px;
    background: var(--brown); color: var(--white); border: 0;
    font: 500 15px 'Jost', sans-serif; letter-spacing: .6px;
  }
  .copyright { position: absolute; left: 88px; top: 334px; font-size: 15px; color: var(--link); letter-spacing: .3px; }
  .payments { position: absolute; left: 544px; top: 330px; display: flex; gap: 14px; align-items: center; }
  .payments span { width: 48px; height: 24px; border-radius: 4px; background: #9c7a5a; }
  .payments span.round { width: 32px; height: 32px; border-radius: 50%; }
</style>
</head>
<body>
  <div class="hero-photo" role="img" aria-label="Photo of a smiling woman angler kneeling by a river, holding a trout, with her dog beside her"></div>

  <header class="site-header">
    <a class="brand" href="#"><span class="brand-dot"></span>Lakes, Lures &amp; Boots</a>
    <div class="utility" style="left:548px"><a href="#">Gift Certificates</a><span class="sep">|</span><a href="#">Sign in or Register</a></div>
    <a class="icon-btn" href="#" style="left:847px" aria-label="Search">
      <svg width="14" height="14" viewBox="0 0 14 14" fill="none" stroke="#fff" stroke-width="1.6"><circle cx="8" cy="6" r="4.5"/><line x1="4.8" y1="9.2" x2="1" y2="13"/></svg>
    </a>
    <a class="cart" href="#">
      <svg width="14" height="13" viewBox="0 0 14 13" fill="none" stroke="#fff" stroke-width="1.4"><path d="M0 1h2.5l1.8 7h7.5L13 3H3.4"/><circle cx="5" cy="11" r="1"/><circle cx="11" cy="11" r="1"/></svg>
      Cart $0.00
    </a>
    <a class="icon-btn" href="#" style="left:1039px" aria-label="Social profile"></a>
    <a class="icon-btn" href="#" style="left:1079px" aria-label="Social profile"></a>
    <nav class="main-nav">
      <a href="#">CLOTHING</a><a href="#">HATS</a><a href="#">BUNDLES</a><a href="#">ACCESSORIES &amp; STICKERS</a><a href="#">JEWELRY</a><a href="#">CLEARANCE</a>
    </nav>
  </header>

  <div class="signup-accent"></div>
  <form class="signup-card" action="https://lakesluresandboots.example/email-opt-in/">
    <h1 class="signup-title">Sign Up Today</h1>
    <p class="signup-sub">And receive <em>15% off</em> your next order</p>
    <div class="field">First Name</div>
    <div class="field">Last Name</div>
    <div class="field">Email Address *</div>
    <button class="cta" type="submit">SUBSCRIBE AND SAVE</button>
  </form>

  <footer class="site-footer">
    <div class="col" style="left:88px">
      <h3>Navigate</h3>
      <ul><li>Trips</li><li>Shipping &amp; Returns</li><li>Contact Us</li><li>Blog</li><li>Sitemap</li></ul>
    </div>
    <div class="col" style="left:320px">
      <h3>Categories</h3>
      <ul><li>Clothing</li><li>Hats</li><li>Bundles</li><li>Accessories &amp; Stickers</li><li>Jewelry</li><li>Clearance</li></ul>
    </div>
    <div class="col" style="left:544px">
      <h3>Info</h3>
      <ul><li>Montana</li></ul>
      <p class="phone">Call us at 4065550182</p>
      <h3 class="connect">Connect With Us</h3>
      <div class="social"><span class="active" aria-label="Social profile"></span><span aria-label="Social profile"></span></div>
    </div>
    <div class="col" style="left:792px">
      <h3>Subscribe to our newsletter</h3>
      <p class="news-copy">Get the latest updates on new products and upcoming sales</p>
      <div class="news-input">Your email address...</div>
      <button class="news-btn">SUBSCRIBE</button>
    </div>
    <p class="copyright">© 2021 Lakes, Lures &amp; Boots</p>
    <div class="payments" aria-label="Accepted payment methods">
      <span></span><span></span><span class="round"></span><span></span><span></span>
    </div>
  </footer>
</body>
</html>
```